Premium small-production winery needs a front label redesign

We produce wine from cold-climate varietal grapes, many of which were only developed in the last 50 years. Our winery, called Harrow Ridge Cellars, is housed in an industrial style building serving a premium product. We have 12 styles of wine that can accommodate a wide range of tastes. We would like to see designs that communicate old traditions (winemaking styles) blended with new ideas (newly developed grape varieties). Our ideal customer enjoys an evening that is cultured and classy, yet fun and educational. We will likely favor designs that are 4" x 4.5", but this isn't required - if we see something we love, we would consider changing the dimensions.
I've attached our current labels and 2 logo files. We are only looking for a front-label redesign. Thanks!

Target Market(s)

Our ideal customer enjoys an evening that is cultured and classy, yet fun and educational.

Font styles to use
Serif
Sans Serif
Script
Other font styles liked:
• Our current fonts are Trajan Pro, Tangerine, and Avenir.

Requirements
Must have
• We would love to see a design that could span our entire product line with only a subtle or minor change (such as printing color, or a picture) to distinguish between our 12 products. Emphasis on the part about the change should be subtle among labels.
• Some of the distinguishing characteristics of the wines:
• Color: white, orange, rosé (pink), light red, dark red
• Sweetness: dry, off-dry, semi-sweet, sweet, very sweet
• Flavors: too many to list
• Product names: 9 of the wines are named after the majority grape. The other 3 are blends of multiple grapes, with the following names: "Velmora Blush", "Opal", and "Thistle".
Nice to have
• our wine list: http://harrowridgecellars.example/wine/
Should not have
• We would prefer a design that isn't too busy overall.

```html
<!DOCTYPE html>
<html lang="en">
<head>
<meta charset="utf-8">
<title>Harrow Ridge Cellars – Thistle front label</title>
<link rel="stylesheet" href="https://fonts.googleapis.com/css2?family=Cinzel:wght@400&family=Pinyon+Script&display=swap">
<style>
  :root {
    --backdrop: #000000;
    --label-orange: #ff3d00;
    --wine-deep: #7a0000;
    --wine-mid: #b81f00;
    --ink-white: #ffffff;
    --script-red: #6e0000;
  }
  html, body {
    margin: 0;
    padding: 0;
    width: 1092px;
    height: 1200px;
    overflow: hidden;
    background: var(--backdrop);
  }
  .canvas {
    position: relative;
    width: 1092px;
    height: 1200px;
    background: var(--backdrop);
  }
  .label {
    position: absolute;
    left: 110px;
    top: 110px;
    width: 872px;
    height: 980px;
    background: var(--label-orange);
    overflow: hidden;
  }
  .splash {
    position: absolute;
    display: block;
  }
  .splash--top-left { left: 0; top: 0; width: 240px; height: 300px; }
  .splash--bottom-right { left: 478px; top: 402px; width: 394px; height: 578px; }
  .brand-mark {
    position: absolute;
    left: 310px;
    top: 146px;
    width: 264px;
    height: 368px;
    display: flex;
    align-items: center;
    justify-content: center;
    font-family: "Cinzel", serif;
    font-weight: 400;
    font-size: 40px;
    line-height: 1.2;
    text-align: center;
    color: var(--ink-white);
  }
  .winery-name {
    position: absolute;
    left: 112px;
    top: 578px;
    margin: 0;
    font-family: "Cinzel", serif;
    font-weight: 400;
    font-size: 88px;
    line-height: 114px;
    letter-spacing: -1px;
    color: var(--ink-white);
    white-space: nowrap;
  }
  .winery-name span { display: block; }
  .wine-name {
    position: absolute;
    left: 112px;
    top: 800px;
    margin: 0;
    font-family: "Pinyon Script", cursive;
    font-weight: 400;
    font-size: 100px;
    line-height: 1.2;
    color: var(--script-red);
  }
</style>
</head>
<body>
<div class="canvas">
  <section class="label">
    <svg class="splash splash--top-left" role="img" aria-label="Swirling splash of red wine flowing from the top-left corner" viewBox="0 0 240 300">
      <defs>
        <radialGradient id="splashTopLeft" cx="0" cy="0" r="1">
          <stop offset="0" stop-color="var(--wine-deep)"/>
          <stop offset="0.55" stop-color="var(--wine-mid)" stop-opacity="0.7"/>
          <stop offset="1" stop-color="var(--label-orange)" stop-opacity="0"/>
        </radialGradient>
      </defs>
      <rect width="240" height="300" fill="url(#splashTopLeft)"/>
    </svg>

    <svg class="splash splash--bottom-right" role="img" aria-label="Swirling splash of red wine rising from the bottom-right corner" viewBox="0 0 394 578">
      <defs>
        <radialGradient id="splashBottomRight" cx="1" cy="1" r="1">
          <stop offset="0" stop-color="var(--wine-deep)"/>
          <stop offset="0.6" stop-color="var(--wine-mid)" stop-opacity="0.7"/>
          <stop offset="1" stop-color="var(--label-orange)" stop-opacity="0"/>
        </radialGradient>
      </defs>
      <rect width="394" height="578" fill="url(#splashBottomRight)"/>
    </svg>

    <div class="brand-mark">Harrow<br>Ridge</div>

    <h1 class="winery-name"><span>HARROW RIDGE</span><span>CELLARS</span></h1>
    <p class="wine-name">Thistle</p>
  </section>
</div>
</body>
</html>
```